Flyer Design

I will be hosting an event at Penrith's amber lantern. Here is a link to their page http://www.theamberlantern.com.au/events-and-workshops/whats-on-penrith/. I have attached the details of my course from their website below. I hope this is of some valuable assistance.

Florist and lover of all things gorgeous, Molly Hartwell from Molly Hartwell Flowers will be running this beautiful and fun workshop. Come along to learn how to make your very own floral crown. All you need to bring are some closed in shoes, an apron and an open mind ready for creativity!

Teens & adults welcome

Date 1: Saturday 11 April 2015
Time 1: 11:00-2:00pm

Date 2: Thursday 23 April 2015
Time 2: 6:00-9:00pm

Cost: $90 per person (includes materials provided – see list below)
Place: The Amber Lantern, Unit 3, 27 Baxter Lane Penrith
RSVP: Molly via email mollyhartwellflowers@fernmail.example or phone 0431 795 206

Materials provided:
• Florist scissors
• Parafilm
• Wire
• Flowers
• light snacks & refreshments

```html
<!DOCTYPE html>
<html lang="en">
<head>
<meta charset="utf-8">
<title>Floral Crown Workshop – Flyer</title>
<link rel="stylesheet" href="https://fonts.googleapis.com/css2?family=Montserrat:wght@400;500;700;800&family=Courgette&display=swap">
<style>
  :root {
    --page-bg: #ece7df;
    --paper: #fdf8e8;
    --pattern-a: #f7e6a6;
    --pattern-b: #fbf2d2;
    --purple: #5b2a86;
    --purple-deep: #3f1a63;
    --violet: #8a4fb8;
    --yellow-band: #f6ea4a;
    --ink: #1f1a24;
    --cup-a: #c6d94a;
    --cup-b: #7fa33a;
    --cup-c: #f2d24a;
    --white: #ffffff;
  }
  * { box-sizing: border-box; margin: 0; padding: 0; }
  html, body { width: 1200px; height: 1000px; overflow: hidden; }
  body {
    background: var(--page-bg);
    font-family: "Montserrat", Arial, sans-serif;
    color: var(--ink);
    position: relative;
  }
  .flyer {
    position: absolute;
    left: 60px; top: 120px;
    width: 1080px; height: 760px;
    background: var(--paper);
    box-shadow: 0 6px 24px rgba(0,0,0,.18);
    overflow: hidden;
  }
  .flyer__pattern {
    position: absolute; inset: 0;
    background:
      radial-gradient(circle at 20% 15%, var(--pattern-a) 0 18%, transparent 40%),
      radial-gradient(circle at 85% 90%, var(--pattern-a) 0 14%, transparent 38%),
      linear-gradient(135deg, var(--pattern-b), var(--paper) 60%, var(--pattern-b));
  }
  .flyer__swoosh { position: absolute; inset: 0; width: 100%; height: 100%; }
  .flyer__photo {
    position: absolute;
    left: 20px; top: 150px;
    width: 360px; height: 600px;
    border-radius: 40% 40% 20% 20% / 20% 20% 10% 10%;
    background: linear-gradient(180deg, var(--white) 0 12%, var(--cup-c) 30%, var(--cup-a) 55%, var(--cup-b) 80%, #5f7a2c 100%);
    opacity: .9;
  }
  .brand {
    position: absolute;
    right: -30px; top: -40px;
    width: 250px; height: 250px;
    border-radius: 50%;
    background: var(--white);
    border: 6px solid var(--purple);
    display: flex; align-items: center; justify-content: flex-start;
    padding-left: 46px; padding-top: 36px;
    gap: 10px;
  }
  .brand__mark { width: 22px; height: 22px; background: var(--purple); flex: none; }
  .brand__name {
    font-weight: 700; font-size: 22px; line-height: 1.05;
    color: var(--purple); width: 110px;
  }
  .content {
    position: absolute;
    left: 400px; top: 140px;
    width: 620px;
  }
  .intro {
    font-weight: 700; font-size: 17px; line-height: 1.45;
    text-align: center;
  }
  .intro strong { color: var(--purple); font-weight: 800; }
  .ribbon {
    margin: 22px auto 0;
    width: 420px; height: 62px;
    background: var(--purple);
    color: var(--white);
    font-family: "Courgette", cursive;
    font-size: 34px;
    display: flex; align-items: center; justify-content: center;
    clip-path: polygon(0 0, 100% 0, 95% 50%, 100% 100%, 0 100%, 5% 50%);
  }
  .dates {
    margin: 18px -60px 0 -40px;
    background: var(--yellow-band);
    display: grid; grid-template-columns: 1fr 1fr;
    padding: 12px 0;
  }
  .dates__item {
    text-align: center; font-weight: 800; font-size: 22px; line-height: 1.25;
  }
  .dates__item + .dates__item { border-left: 2px solid var(--ink); }
  .dates__time { font-weight: 500; }
  .details {
    margin-top: 16px;
    font-size: 15px; line-height: 1.5; text-align: center;
  }
  .details b { font-weight: 800; }
  .details .label { color: var(--purple); font-weight: 800; }
  .details .strong { font-weight: 700; }
  .materials {
    margin: 14px auto 0; width: 440px;
    border-top: 3px dotted var(--ink);
    padding-top: 10px;
  }
  .materials__title {
    text-align: center; color: var(--purple);
    font-weight: 800; font-size: 19px;
  }
  .materials__list {
    list-style: none;
    display: grid; grid-template-columns: 1fr 1fr;
    font-size: 16px; line-height: 1.4; margin-top: 6px; padding-left: 40px;
  }
  .materials__list li::before { content: "• "; }
</style>
</head>
<body>
  <main class="flyer">
    <div class="flyer__pattern" role="img" aria-label="Soft pale yellow floral background pattern"></div>

    <svg class="flyer__swoosh" viewBox="0 0 1080 760" preserveAspectRatio="none" aria-hidden="true">
      <path d="M0 150 C 260 60, 600 120, 1080 20 L1080 0 L0 0 Z" fill="var(--paper)" opacity=".6"/>
      <path d="M0 170 C 280 70, 620 135, 1080 30" fill="none" stroke="var(--purple)" stroke-width="14"/>
      <path d="M0 190 C 290 95, 640 155, 1080 55" fill="none" stroke="var(--violet)" stroke-width="5"/>
      <path d="M360 760 C 560 690, 820 720, 1080 600" fill="none" stroke="var(--purple)" stroke-width="14"/>
      <path d="M380 760 C 580 710, 830 745, 1080 625" fill="none" stroke="var(--violet)" stroke-width="5"/>
    </svg>

    <div class="flyer__photo" role="img" aria-label="Photo of stacked yellow and green teacups with white daisies"></div>

    <div class="brand">
      <span class="brand__mark"></span>
      <span class="brand__name">the amber lantern</span>
    </div>

    <section class="content">
      <p class="intro">Florist and lover of all things gorgeous, <strong>Molly Hartwell</strong> from <strong>Molly Hartwell Flowers</strong> will be running this beautiful and fun workshop. Come along to learn how to make your very own floral crown. All you need to bring are some closed in shoes, an apron and an open mind ready for creativity!</p>

      <div class="ribbon">Teens &amp; adults welcome</div>

      <div class="dates">
        <div class="dates__item">Saturday 11 April 2015<br><span class="dates__time">11:00-2:00pm</span></div>
        <div class="dates__item">Thursday 23 April 2015<br><span class="dates__time">6:00-9:00pm</span></div>
      </div>

      <p class="details">
        <b>Cost: $90 per person</b> (includes materials provided – see list below)<br>
        <span class="label">Place:</span> The Amber Lantern, Unit 3, 27 Baxter Lane Penrith<br>
        <span class="label">RSVP:</span> Molly via email <span class="strong">mollyhartwellflowers@fernmail.example</span><br>
        or phone <span class="strong">0431 795 206</span>
      </p>

      <div class="materials">
        <h2 class="materials__title">Materials provided:</h2>
        <ul class="materials__list">
          <li>Florist scissors</li>
          <li>Flowers</li>
          <li>Parafilm</li>
          <li>Light snacks &amp; refreshments</li>
          <li>Wire</li>
        </ul>
      </div>
    </section>
  </main>
</body>
</html>
```